New Banner Ad Design Project

I need to design two banners for advertising on the website ( 728x90 and 300x250). The banners should have the following text that switches from one to another in simple animation:

Be The Cutting Edge Risk Organization
Request Your Tour of Ledger Shock Trials

It should also have our logo somewhere (pdf file attached). No pictures or unnecessary clutter.
The banner should have something that looks like a button that invites a click.
The banners should be a combination of white, blue and orange color. Nothing complicated, but business like and appealing/clickable.
Detailed banner specs are in the attached png file. Please only take this if you have designed successful (clickable) banner ads before.
The banners are simple, but the job is rather urgent.

Marcus

```html
<!DOCTYPE html>
<html lang="en">
<head>
<meta charset="utf-8">
<title>Veltrisk Banner Set</title>
<link rel="stylesheet" href="https://fonts.googleapis.com/css2?family=League+Gothic&display=swap">
<style>
  :root {
    --stage-bg: #d6d6d6;
    --blue-top: #0a9ad8;
    --blue-bottom: #08679a;
    --blue-wide-bottom: #0a82bf;
    --white: #ffffff;
    --ink: #232323;
    --mark: #3e7d2e;
    --orange: #ff8300;
    --orange-edge: #d96a00;
    --headline-shadow: rgba(0, 40, 70, 0.55);
  }
  * { box-sizing: border-box; margin: 0; padding: 0; }
  html, body {
    width: 1200px;
    height: 783px;
    overflow: hidden;
    background: var(--stage-bg);
    font-family: "League Gothic", "Oswald", sans-serif;
  }
  .stage { position: relative; width: 1200px; height: 783px; }

  .banner {
    position: absolute;
    overflow: hidden;
    background: linear-gradient(to bottom, var(--blue-top), var(--blue-bottom));
    box-shadow: 0 1px 4px rgba(0, 0, 0, 0.15);
    color: var(--white);
  }
  .banner--tall { width: 277px; height: 231px; top: 102px; }
  .banner--wide {
    width: 672px; height: 83px; left: 264px;
    background: linear-gradient(to bottom, var(--blue-top), var(--blue-wide-bottom));
  }

  .banner__corner { position: absolute; left: 0; top: 0; }

  .brand {
    position: absolute;
    display: flex;
    align-items: center;
    gap: 5px;
    transform: rotate(-20deg);
    transform-origin: left center;
    color: var(--ink);
    font-size: 26px;
    line-height: 1;
    letter-spacing: 0.5px;
  }
  .brand__dot {
    width: 10px; height: 10px;
    background: var(--mark);
  }
  .banner--tall .brand { left: 6px; top: 42px; }
  .banner--wide .brand { left: 4px; top: 36px; font-size: 24px; }

  .headline {
    position: absolute;
    text-align: center;
    text-transform: uppercase;
    text-shadow: 1px 2px 2px var(--headline-shadow);
    white-space: nowrap;
  }
  .banner--tall .headline {
    left: 0; right: 0; top: 70px;
    font-size: 35px;
    line-height: 40px;
  }
  .banner--wide .headline {
    left: 90px; width: 440px; top: 0;
    font-size: 29px;
    line-height: 83px;
  }
  .headline--fading { opacity: 0.55; }

  .cta {
    position: absolute;
    display: flex;
    align-items: center;
    justify-content: center;
    background: var(--orange);
    border-bottom: 3px solid var(--orange-edge);
    border-radius: 2px;
    color: var(--white);
    text-transform: uppercase;
    letter-spacing: 0.3px;
  }
  .banner--tall .cta {
    left: 55px; top: 162px; width: 167px; height: 46px;
    font-size: 26px;
  }
  .banner--wide .cta {
    left: 533px; top: 25px; width: 117px; height: 33px;
    font-size: 18px;
  }
</style>
</head>
<body>
<main class="stage">

  <!-- 300x250 sequence -->
  <section class="banner banner--tall" style="left:149px">
    <svg class="banner__corner" width="277" height="231" aria-hidden="true"><polygon points="0,0 176,0 0,70" fill="#ffffff"/></svg>
    <div class="brand"><span class="brand__dot"></span>Veltrisk</div>
    <h2 class="headline">Be the cutting edge<br>risk organization</h2>
    <span class="cta">Request now</span>
  </section>

  <section class="banner banner--tall" style="left:462px">
    <svg class="banner__corner" width="277" height="231" aria-hidden="true"><polygon points="0,0 176,0 0,70" fill="#ffffff"/></svg>
    <div class="brand"><span class="brand__dot"></span>Veltrisk</div>
    <h2 class="headline headline--fading">Be the cutting edge<br>risk organization</h2>
    <h2 class="headline headline--fading">Request your tour of<br>Ledger Shock Trials</h2>
    <span class="cta">Request now</span>
  </section>

  <section class="banner banner--tall" style="left:782px">
    <svg class="banner__corner" width="277" height="231" aria-hidden="true"><polygon points="0,0 176,0 0,70" fill="#ffffff"/></svg>
    <div class="brand"><span class="brand__dot"></span>Veltrisk</div>
    <h2 class="headline">Request your tour of<br>Ledger Shock Trials</h2>
    <span class="cta">Request now</span>
  </section>

  <!-- 728x90 sequence -->
  <section class="banner banner--wide" style="top:391px">
    <svg class="banner__corner" width="672" height="83" aria-hidden="true"><polygon points="0,0 152,0 0,60" fill="#ffffff"/></svg>
    <div class="brand"><span class="brand__dot"></span>Veltrisk</div>
    <h2 class="headline">Be the cutting edge risk organization</h2>
    <span class="cta">Request now</span>
  </section>

  <section class="banner banner--wide" style="top:506px">
    <svg class="banner__corner" width="672" height="83" aria-hidden="true"><polygon points="0,0 152,0 0,60" fill="#ffffff"/></svg>
    <div class="brand"><span class="brand__dot"></span>Veltrisk</div>
    <h2 class="headline headline--fading">Be the cutting edge risk organization</h2>
    <h2 class="headline headline--fading">Request your tour of Ledger Shock Trials</h2>
    <span class="cta">Request now</span>
  </section>

  <section class="banner banner--wide" style="top:622px">
    <svg class="banner__corner" width="672" height="83" aria-hidden="true"><polygon points="0,0 152,0 0,60" fill="#ffffff"/></svg>
    <div class="brand"><span class="brand__dot"></span>Veltrisk</div>
    <h2 class="headline">Request your tour of Ledger Shock Trials</h2>
    <span class="cta">Request now</span>
  </section>

</main>
</body>
</html>
```